TRW General Contracting

Roofing, Siding,windows, doors, Gutter,additions, decks, garagesand hanyman services fully insured and licensed, free estimates, accept all major credit cards call (614)392-7705 email corvinwr@mailbrook.net

Target Market(s)

Home improvement

Industry/Entity Type

Home Improvement

Requirements
Must have
• Whats listed above
Nice to have
• I dont have a logo i want wording for roofing, siding, gutter, decks, additions, windows, doors, and handyman services with my phone # 614-392-7705 and email corvinwr@mailbrook.net

```html
<!DOCTYPE html>
<html lang="en">
<head>
<meta charset="utf-8">
<title>Home Improvement Postcard – Front and Back</title>
<link href="https://fonts.googleapis.com/css2?family=Alfa+Slab+One&family=Ubuntu:wght@400;500;700&display=swap" rel="stylesheet">
<style>
  :root{
    --slate:#333b46;
    --slate-dark:#2b323c;
    --yellow:#ecdc10;
    --lime:#c9d62c;
    --navy:#1f3b7a;
    --paper:#ffffff;
    --mist:#e9e9ea;
    --line:#c9c9cb;
    --ink:#141414;
    --stage:#3a3a3c;
  }
  *{box-sizing:border-box;margin:0;padding:0}
  html,body{width:1200px;height:1200px;overflow:hidden;background:var(--stage)}
  body{position:relative;font-family:'Ubuntu',sans-serif}

  .postcard{position:absolute;left:180px;width:840px;height:562px;overflow:hidden;box-shadow:0 6px 18px rgba(0,0,0,.35)}
  .postcard--front{top:22px;background:var(--mist)}
  .postcard--back{top:614px;background:var(--paper)}

  /* front */
  .front-header{position:absolute;left:0;top:0;width:100%;height:137px;background:var(--slate);text-align:center}
  .front-header__lead{font-family:'Alfa Slab One',serif;color:#fff;font-size:40px;line-height:1;padding-top:18px}
  .front-header__title{font-family:'Alfa Slab One',serif;color:var(--yellow);font-size:43px;line-height:1;margin-top:14px;letter-spacing:.3px}

  .photo{position:absolute}
  .photo--worker{left:6px;top:144px;width:350px;height:311px;background:linear-gradient(135deg,#b8773a 0%,#8a5a2c 45%,#1f7a4a 75%,#c7b334 100%)}
  .photo--roof{left:664px;top:144px;width:172px;height:101px;background:linear-gradient(160deg,#c9c0b6 0%,#b33a3a 70%,#8d2a2a 100%)}
  .photo--gutter{left:664px;top:250px;width:172px;height:101px;background:linear-gradient(160deg,#4d5b6b 0%,#2d4c80 55%,#8f9aa6 100%)}
  .photo--siding{left:664px;top:356px;width:172px;height:99px;background:linear-gradient(160deg,#8a6a4e 0%,#d8cfae 55%,#b23232 100%)}

  .services{position:absolute;left:363px;top:144px;width:297px;height:311px;background:var(--slate);color:#fff}
  .services__heading{text-align:center;font-weight:500;font-size:19px;padding-top:12px}
  .services__list{display:grid;grid-template-columns:150px 130px;row-gap:9px;padding:25px 0 0 14px;list-style:none;font-size:18px}
  .services__item{display:flex;align-items:center;gap:7px}
  .services__item--wide{grid-column:1 / 3}
  .badge{width:15px;height:15px;border-radius:50%;background:var(--yellow);color:var(--slate);font-size:10px;font-weight:700;display:inline-flex;align-items:center;justify-content:center}
  .services__insured{position:absolute;left:0;top:222px;width:100%;height:30px;border-top:1px solid #5b6470;border-bottom:1px solid #5b6470;font-family:'Alfa Slab One',serif;color:var(--yellow);font-size:13.5px;text-align:center;line-height:30px}
  .services__estimates{position:absolute;left:0;top:258px;width:100%;text-align:center;font-family:'Alfa Slab One',serif;color:#e6e6e6;font-size:25px;line-height:44px}

  .payment-note{position:absolute;left:0;top:455px;width:100%;height:49px;background:var(--paper);text-align:center;font-weight:500;font-size:27px;color:var(--ink);line-height:48px}
  .front-footer{position:absolute;left:0;top:504px;width:100%;height:58px;background:var(--slate);color:#fff;font-size:25px;font-weight:500;display:flex;align-items:center;padding-left:16px;white-space:nowrap}
  .front-footer__divider{display:inline-block;width:1px;height:30px;background:#fff;margin:0 10px}

  /* back */
  .mailing-side{position:absolute;left:405px;top:0;width:435px;height:431px;background:var(--mist)}
  .stamp-box{position:absolute;right:0;top:0;width:194px;height:172px;border-left:1px solid var(--line);border-bottom:1px solid var(--line)}
  .address-line{position:absolute;left:14px;right:0;height:1px;background:var(--line)}

  .promo-panel{position:absolute;left:0;top:0;width:405px;height:431px}
  .promo-panel__label{height:50px;background:var(--lime);font-family:'Alfa Slab One',serif;color:var(--slate-dark);font-size:17px;line-height:50px;padding-left:8px;letter-spacing:.2px}
  .photo--house{position:relative;width:405px;height:233px;background:linear-gradient(180deg,#8fb3dc 0%,#c9d7e6 38%,#b9a48a 55%,#6f6a63 72%,#4f8a3a 88%,#3b6e2b 100%)}
  .promo-panel__cta{height:50px;background:var(--lime);font-family:'Alfa Slab One',serif;color:var(--slate-dark);font-size:37px;line-height:52px;text-align:center;letter-spacing:.5px}
  .promo-panel__phone{height:58px;background:var(--slate);color:#fff;font-weight:700;font-size:44px;line-height:58px;text-align:center}
  .promo-panel__email{height:40px;background:var(--navy);color:#fff;font-weight:500;font-size:21px;line-height:40px;text-align:center}
</style>
</head>
<body>

<section class="postcard postcard--front" aria-label="Postcard front">
  <header class="front-header">
    <p class="front-header__lead">We Solve</p>
    <h1 class="front-header__title">ALL YOUR HOUSE PROBLEMS!</h1>
  </header>

  <div class="photo photo--worker" role="img" aria-label="Photo of a young tradesman in a green and yellow uniform fitting a lock into a wooden door"></div>

  <div class="services">
    <h2 class="services__heading">We Specialize in:</h2>
    <ul class="services__list">
      <li class="services__item"><span class="badge">1</span>Roofing</li>
      <li class="services__item"><span class="badge">6</span>Gutter</li>
      <li class="services__item"><span class="badge">2</span>Sliding</li>
      <li class="services__item"><span class="badge">7</span>Additions</li>
      <li class="services__item"><span class="badge">3</span>Windows</li>
      <li class="services__item"><span class="badge">8</span>Decks</li>
      <li class="services__item"><span class="badge">4</span>Doors</li>
      <li class="services__item"><span class="badge">9</span>Garages</li>
      <li class="services__item services__item--wide"><span class="badge">5</span>Handyman Services</li>
    </ul>
    <p class="services__insured">FULLY INSURED AND LICENSED</p>
    <p class="services__estimates">FREE ESTIMATES</p>
  </div>

  <div class="photo photo--roof" role="img" aria-label="Photo of a worker installing red roof tiles"></div>
  <div class="photo photo--gutter" role="img" aria-label="Photo of a man cleaning a house gutter"></div>
  <div class="photo photo--siding" role="img" aria-label="Photo of a worker on a ladder installing siding"></div>

  <p class="payment-note">We accept all major credit cards</p>

  <footer class="front-footer">
    <span>CALL TODAY - (614)392-7705</span>
    <span class="front-footer__divider"></span>
    <span>email : corvinwr@mailbrook.net</span>
  </footer>
</section>

<section class="postcard postcard--back" aria-label="Postcard back">
  <div class="promo-panel">
    <p class="promo-panel__label">HOME IMPROVEMENT SERVICES</p>
    <div class="photo--house" role="img" aria-label="Photo of a two-storey suburban house with stone front and landscaped garden"></div>
    <p class="promo-panel__cta">CALL TODAY</p>
    <p class="promo-panel__phone">614-392-7705</p>
    <p class="promo-panel__email">corvinwr@mailbrook.net</p>
  </div>

  <div class="mailing-side" aria-label="Address area">
    <div class="stamp-box"></div>
    <div class="address-line" style="top:248px"></div>
    <div class="address-line" style="top:294px"></div>
    <div class="address-line" style="top:340px"></div>
    <div class="address-line" style="top:386px"></div>
    <div class="address-line" style="top:430px"></div>
  </div>
</section>

</body>
</html>
```